UI design for a mobile app that manages color schemes/pallettes

Should look cool, different, and modern.
The UI colors should not compete with pallette colors (as much as possible)
Features:
Currently looking for 3 pages/screens for the app: Browse through all palettes, view/edit a single palette, import
Features to include in the UI:
- View the list of color palettes (each list item includes a preview showing all colors in that color palette)
- View a particular color palette.
- Each displayed color should show:
- hex value
- rgb(255, 255, 255) value
- Name of pallete
- Button to copy the palette to a new pallette
- Sliders to change the properties (hue, saturation, value) or all colors in the palette at once
- Ability to add color
- Ability to remove color
- Switch background color that the pallete is displayed on: (black, mid gray, white, custom)
- A page that allows you to import palettes from a folder
Look and feel
Each slider illustrates characteristics of the customer's brand and the style your logo design should communicate.

```html
<!DOCTYPE html>
<html lang="en">
<head>
<meta charset="utf-8">
<title>Huebox – Palette App Screens</title>
<link rel="stylesheet" href="https://fonts.googleapis.com/css2?family=Poppins:wght@500;600;700&family=Nunito+Sans:wght@400;600;700&display=swap">
<style>
  :root{
    --bg:#f5eeea;
    --screen:#ffffff;
    --orange:#ff7a3d;
    --orange-light:#ff9a6a;
    --orange-deep:#ff6b35;
    --pill:#fde6dc;
    --ink:#2a2a2a;
    --text:#3a3a3a;
    --line:#d9d9d9;
    --track:#dedede;
    --wine:#900c2a;
    --grey-add:#7a7474;
  }
  *{box-sizing:border-box;margin:0;padding:0}
  html,body{width:1200px;height:803px;overflow:hidden;background:var(--bg)}
  body{position:relative;font-family:"Nunito Sans",sans-serif;color:var(--text)}

  .screen{position:absolute;width:300px;height:650px;background:var(--screen);border-radius:30px;overflow:hidden;box-shadow:0 6px 18px rgba(120,80,60,.12)}
  .screen--all{left:103px;top:60px}
  .screen--edit{left:452px;top:67px}
  .screen--import{left:804px;top:73px}

  .header{position:absolute;left:0;top:0;width:300px;height:160px}
  .header svg{position:absolute;left:0;top:0}
  .brand{position:absolute;left:0;width:100%;top:26px;display:flex;justify-content:center;align-items:center;gap:7px;font-family:"Poppins",sans-serif;font-weight:600;font-size:17px;color:#fff}
  .brand-dot{width:18px;height:18px;border-radius:50%;background:#fff}
  .menu{position:absolute;right:18px;top:29px;width:27px;height:13px;display:flex;flex-direction:column;justify-content:space-between}
  .menu span{display:block;height:2px;background:#fff;border-radius:1px}
  .screen-title{position:absolute;left:0;width:100%;top:74px;text-align:center;font-family:"Poppins",sans-serif;font-weight:700;font-size:20px;color:#fff;letter-spacing:.2px}
  .title-rule{position:absolute;left:50%;top:106px;width:40px;margin-left:-20px;height:2px;background:#fff}

  .card{position:absolute;left:14px;width:269px;border:1px solid var(--line);background:#fff}
  .card--active{border:1.5px solid var(--orange)}
  .swatch{position:absolute;left:13px;top:50%;width:87px;height:87px;margin-top:-44px;border-radius:50%}
  .card-info{position:absolute;left:121px;top:12px}
  .card-title{font-family:"Poppins",sans-serif;font-weight:600;font-size:14px;color:var(--ink);line-height:18px}
  .card-meta{font-size:11.5px;line-height:17px;color:var(--text)}
  .copy-pill{display:inline-block;margin-top:6px;height:19px;padding:0 16px;border-radius:10px;background:var(--pill);font-size:8.5px;line-height:19px;color:#555}
  .eye{position:absolute;right:14px;bottom:14px}

  .btn{position:absolute;border-radius:20px;background:var(--orange);color:#fff;font-family:"Poppins",sans-serif;font-weight:600;text-align:center}
  .btn--more{left:93px;width:110px;height:30px;line-height:30px;font-size:10px}

  /* edit */
  .panel{position:absolute;left:9px;top:141px;width:280px;height:464px;border:1px solid var(--line)}
  .color-name{position:absolute;left:0;width:100%;top:14px;text-align:center;font-family:"Poppins",sans-serif;font-weight:600;font-size:19px;color:var(--ink)}
  .color-code{position:absolute;left:0;width:100%;text-align:center;font-size:11.5px;font-weight:600;color:var(--ink)}
  .chip{position:absolute;top:102px;width:88px;height:88px;border-radius:50%;color:#fff;font-family:"Poppins",sans-serif;font-weight:600;font-size:12px;display:flex;flex-direction:column;align-items:center;justify-content:center;text-align:center}
  .chip--add{font-size:10.5px;gap:3px}
  .chip-btn{position:absolute;top:198px;width:68px;height:20px;border-radius:10px;background:var(--pill);font-size:9.5px;line-height:20px;text-align:center;color:#555}
  .gradient-bar{position:absolute;left:24px;top:235px;width:235px;height:13px;border-radius:7px;background:linear-gradient(90deg,#ff7a3d,#c0392b 55%,#900c2a)}
  .stop{position:absolute;top:248px;width:1px;height:6px;background:var(--wine)}
  .stop-label{position:absolute;top:258px;font-size:7.5px;font-weight:700;color:var(--wine)}
  .stop-add{position:absolute;left:127px;top:259px}
  .slider{position:absolute;left:24px;width:233px}
  .slider-label{font-family:"Poppins",sans-serif;font-weight:600;font-size:10px;color:var(--ink)}
  .slider-value{position:absolute;right:2px;top:0;font-size:11px;color:var(--ink)}
  .slider-track{position:absolute;left:0;top:18px;width:100%;height:4px;background:var(--track);border-radius:2px}
  .slider-thumb{position:absolute;left:110px;top:12px;width:3px;height:15px;background:var(--orange-deep);border-radius:1px}
  .btn--import-main{left:66px;top:413px;width:141px;height:34px;line-height:34px;font-size:10px;padding-left:22px;border-radius:18px}
  .btn-plus{position:absolute;left:7px;top:7px;width:20px;height:20px;border-radius:50%;background:#fff;color:var(--orange);font-size:15px;line-height:19px;text-align:center;font-weight:500}

  /* import */
  .pair{position:absolute;top:50%;width:67px;height:67px;margin-top:-34px;border-radius:50%}
  .pair--back{left:16px}
  .pair--front{left:61px;opacity:.86}
  .card-info--import{left:135px;top:12px}
  .import-pill{display:inline-block;margin-top:6px;width:97px;height:26px;border-radius:13px;background:var(--orange);color:#fff;font-family:"Poppins",sans-serif;font-weight:600;font-size:7.5px;line-height:26px;text-align:center}
</style>
</head>
<body>

<!-- Screen: all palettes -->
<section class="screen screen--all">
  <div class="header">
    <svg width="300" height="160" viewBox="0 0 300 160"><defs><linearGradient id="hg1" x1="0" x2="1"><stop offset="0" stop-color="#ff7040"/><stop offset="1" stop-color="#ff9d6c"/></linearGradient></defs><path d="M0 0H300V98Q150 157 0 92Z" fill="url(#hg1)"/></svg>
    <div class="brand"><span class="brand-dot"></span>Huebox</div>
    <div class="menu"><span></span><span></span><span></span></div>
    <h1 class="screen-title">ALL PALETTES</h1>
    <div class="title-rule"></div>
  </div>

  <article class="card card--active" style="top:145px;height:102px">
    <div class="swatch" style="background:linear-gradient(90deg,#8e0c2a 0 34%,#c8001f 34% 67%,#ff7733 67%)"></div>
    <div class="card-info"><h2 class="card-title">Palettes Title</h2><p class="card-meta">Hex: #ff8552</p><p class="card-meta">rgb: (255, 255, 255)</p><span class="copy-pill">Copy Pallete</span></div>
    <svg class="eye" width="21" height="13" viewBox="0 0 21 13"><path d="M1 6.5C4 1.5 17 1.5 20 6.5C17 11.5 4 11.5 1 6.5Z" fill="none" stroke="#111" stroke-width="1.6"/><circle cx="10.5" cy="6.5" r="3" fill="none" stroke="#111" stroke-width="1.6"/></svg>
  </article>

  <article class="card" style="top:253px;height:101px">
    <div class="swatch" style="background:linear-gradient(90deg,#9aafad 0 26%,#6f9096 26% 58%,#688e6c 58% 88%,#2e5d5c 88%)"></div>
    <div class="card-info"><h2 class="card-title">Palettes Title</h2><p class="card-meta">Hex: #ff8552</p><p class="card-meta">rgb: (255, 255, 255)</p><span class="copy-pill">Copy Pallete</span></div>
    <svg class="eye" width="21" height="13" viewBox="0 0 21 13"><path d="M1 6.5C4 1.5 17 1.5 20 6.5C17 11.5 4 11.5 1 6.5Z" fill="none" stroke="#111" stroke-width="1.6"/><circle cx="10.5" cy="6.5" r="3" fill="none" stroke="#111" stroke-width="1.6"/></svg>
  </article>

  <article class="card" style="top:361px;height:101px">
    <div class="swatch" style="background:linear-gradient(90deg,#4fadc8 0 16%,#3c88a0 16% 46%,#2a5e78 46% 76%,#1e3a50 76%)"></div>
    <div class="card-info"><h2 class="card-title">Palettes Title</h2><p class="card-meta">Hex: #ff8552</p><p class="card-meta">rgb: (255, 255, 255)</p><span class="copy-pill">Copy Pallete</span></div>
    <svg class="eye" width="21" height="13" viewBox="0 0 21 13"><path d="M1 6.5C4 1.5 17 1.5 20 6.5C17 11.5 4 11.5 1 6.5Z" fill="none" stroke="#111" stroke-width="1.6"/><circle cx="10.5" cy="6.5" r="3" fill="none" stroke="#111" stroke-width="1.6"/></svg>
  </article>

  <article class="card" style="top:474px;height:101px">
    <div class="swatch" style="background:linear-gradient(90deg,#f8aeb6 0 34%,#f6b6ba 34% 67%,#ffc8cc 67%)"></div>
    <div class="card-info"><h2 class="card-title">Palettes Title</h2><p class="card-meta">Hex: #ff8552</p><p class="card-meta">rgb: (255, 255, 255)</p><span class="copy-pill">Copy Pallete</span></div>
    <svg class="eye" width="21" height="13" viewBox="0 0 21 13"><path d="M1 6.5C4 1.5 17 1.5 20 6.5C17 11.5 4 11.5 1 6.5Z" fill="none" stroke="#111" stroke-width="1.6"/><circle cx="10.5" cy="6.5" r="3" fill="none" stroke="#111" stroke-width="1.6"/></svg>
  </article>

  <div class="btn btn--more" style="top:590px">VIEW MORE</div>
</section>

<!-- Screen: edit palette -->
<section class="screen screen--edit">
  <div class="header">
    <svg width="300" height="160" viewBox="0 0 300 160"><defs><linearGradient id="hg2" x1="0" x2="1"><stop offset="0" stop-color="#ff7040"/><stop offset="1" stop-color="#ff9d6c"/></linearGradient></defs><path d="M0 0H300V98Q150 157 0 92Z" fill="url(#hg2)"/></svg>
    <div class="brand"><span class="brand-dot"></span>Huebox</div>
    <div class="menu"><span></span><span></span><span></span></div>
    <h1 class="screen-title">EDIT PALETTES</h1>
    <div class="title-rule"></div>
  </div>

  <div class="panel">
    <h2 class="color-name">Red Orangle Color</h2>
    <p class="color-code" style="top:46px">Hex: #ff8552</p>
    <p class="color-code" style="top:63px">rgb: (255, 255, 255)</p>

    <div class="chip" style="left:14px;background:var(--wine)">#900c2a</div>
    <div class="chip" style="left:96px;background:var(--orange)">#900c2a</div>
    <div class="chip chip--add" style="left:178px;background:var(--grey-add)">
      <svg width="17" height="17" viewBox="0 0 17 17"><circle cx="8.5" cy="8.5" r="7.5" fill="none" stroke="#fff" stroke-width="1.3"/><path d="M8.5 4.5V12.5M4.5 8.5H12.5" stroke="#fff" stroke-width="1.3"/></svg>
      Add color
    </div>
    <div class="chip-btn" style="left:24px">Remove</div>
    <div class="chip-btn" style="left:104px">Remove</div>
    <div class="chip-btn" style="left:185px">Add new</div>

    <div class="gradient-bar"></div>
    <div class="stop" style="left:28px"></div>
    <div class="stop" style="left:256px"></div>
    <span class="stop-label" style="left:11px">#900c2a</span>
    <span class="stop-label" style="left:226px">#900c2a</span>
    <svg class="stop-add" width="13" height="13" viewBox="0 0 13 13"><circle cx="6.5" cy="6.5" r="5.8" fill="none" stroke="#ff6b35" stroke-width="1.1"/><path d="M6.5 3.5V9.5M3.5 6.5H9.5" stroke="#ff6b35" stroke-width="1.1"/></svg>

    <div class="slider" style="top:292px"><span class="slider-label">Hue</span><span class="slider-value">0</span><div class="slider-track"></div><div class="slider-thumb"></div></div>
    <div class="slider" style="top:329px"><span class="slider-label">Saturation</span><span class="slider-value">0</span><div class="slider-track"></div><div class="slider-thumb"></div></div>
    <div class="slider" style="top:365px"><span class="slider-label">Lightness</span><span class="slider-value">0</span><div class="slider-track"></div><div class="slider-thumb"></div></div>

    <div class="btn btn--import-main"><span class="btn-plus">+</span>IMPORT PALETTE</div>
  </div>
</section>

<!-- Screen: import palette -->
<section class="screen screen--import">
  <div class="header">
    <svg width="300" height="160" viewBox="0 0 300 160"><defs><linearGradient id="hg3" x1="0" x2="1"><stop offset="0" stop-color="#ff7040"/><stop offset="1" stop-color="#ff9d6c"/></linearGradient></defs><path d="M0 0H300V98Q150 157 0 92Z" fill="url(#hg3)"/></svg>
    <div class="brand"><span class="brand-dot"></span>Huebox</div>
    <div class="menu"><span></span><span></span><span></span></div>
    <h1 class="screen-title">IMPORT PALETTE</h1>
    <div class="title-rule"></div>
  </div>

  <article class="card" style="left:15px;top:144px;height:105px">
    <div class="pair pair--back" style="background:#900c2a"></div><div class="pair pair--front" style="background:#ff8552"></div>
    <div class="card-info card-info--import"><h2 class="card-title">Palettes Title</h2><p class="card-meta">Hex: #ff8552</p><p class="card-meta">rgb: (255, 255, 255)</p><span class="import-pill">IMPORT PALETTE</span></div>
  </article>
  <article class="card" style="left:15px;top:249px;height:105px">
    <div class="pair pair--back" style="background:#0f8f6a"></div><div class="pair pair--front" style="background:#1fd39a"></div>
    <div class="card-info card-info--import"><h2 class="card-title">Palettes Title</h2><p class="card-meta">Hex: #ff8552</p><p class="card-meta">rgb: (255, 255, 255)</p><span class="import-pill">IMPORT PALETTE</span></div>
  </article>
  <article class="card" style="left:15px;top:354px;height:105px">
    <div class="pair pair--back" style="background:#c12ccf"></div><div class="pair pair--front" style="background:#6236d0"></div>
    <div class="card-info card-info--import"><h2 class="card-title">Palettes Title</h2><p class="card-meta">Hex: #ff8552</p><p class="card-meta">rgb: (255, 255, 255)</p><span class="import-pill">IMPORT PALETTE</span></div>
  </article>
  <article class="card" style="left:15px;top:459px;height:106px">
    <div class="pair pair--back" style="background:#14a0f0"></div><div class="pair pair--front" style="background:#0a45b8"></div>
    <div class="card-info card-info--import"><h2 class="card-title">Palettes Title</h2><p class="card-meta">Hex: #ff8552</p><p class="card-meta">rgb: (255, 255, 255)</p><span class="import-pill">IMPORT PALETTE</span></div>
  </article>

  <div class="btn btn--more" style="top:592px">VIEW MORE</div>
</section>

</body>
</html>
```